Business Card Design Project

Business Card
We are rebranding with a new logo
Industry/Entity Type
Business
Contact Information for Business Card
Dennis Marlow +61 427581962 dennis@qovo.com.au P.O. Box 872 Kelvindale QLD 4309
Requirements
Must have
- Logo

```html
<!DOCTYPE html>
<html lang="en">
<head>
<meta charset="utf-8">
<title>Qovo International – Business Card</title>
<link rel="stylesheet" href="https://fonts.googleapis.com/css2?family=Abel&family=Roboto:wght@400;500&display=swap">
<style>
  :root {
    --page-bg: #c8c8c8;
    --card-bg: #f7f7f7;
    --card-arc: #ffffff;
    --ink: #2b2b2b;
    --ink-soft: #3a3a3a;
    --accent-blue: #1b9ad6;
    --brand-blue: #1670a8;
  }
  * { margin: 0; padding: 0; box-sizing: border-box; }
  html, body {
    width: 1200px;
    height: 1200px;
    overflow: hidden;
    background: var(--page-bg);
  }
  .stage {
    position: relative;
    width: 1200px;
    height: 1200px;
  }
  .business-card {
    position: absolute;
    left: 100px;
    top: 327px;
    width: 1000px;
    height: 546px;
    background: linear-gradient(135deg, #f2f2f2 0%, var(--card-bg) 50%, #f0f0f0 100%);
    box-shadow: 0 6px 16px rgba(0, 0, 0, 0.25);
    overflow: hidden;
  }
  .card-arc {
    position: absolute;
    left: 570px;
    top: -260px;
    width: 1060px;
    height: 1060px;
    border-radius: 50%;
    background: radial-gradient(circle at 30% 50%, var(--card-arc) 0%, #f4f4f4 70%);
    box-shadow: -3px 0 8px rgba(0, 0, 0, 0.06);
  }
  .holder-name {
    position: absolute;
    left: 82px;
    top: 145px;
    font-family: "Abel", sans-serif;
    font-size: 54px;
    letter-spacing: 2px;
    color: var(--ink);
    font-weight: 400;
  }
  .contact-list {
    position: absolute;
    left: 79px;
    top: 262px;
    list-style: none;
  }
  .contact-item {
    display: flex;
    align-items: center;
    height: 38px;
    margin-bottom: 15px;
    font-family: "Roboto", sans-serif;
    font-size: 24px;
    color: var(--ink-soft);
  }
  .contact-badge {
    width: 38px;
    height: 38px;
    border-radius: 50%;
    background: var(--accent-blue);
    color: #fff;
    font-size: 16px;
    font-weight: 500;
    display: flex;
    align-items: center;
    justify-content: center;
    margin-right: 24px;
    flex-shrink: 0;
  }
  .brand-mark {
    position: absolute;
    left: 640px;
    top: 240px;
    display: flex;
    align-items: center;
    gap: 18px;
  }
  .brand-dot {
    width: 34px;
    height: 34px;
    border-radius: 50%;
    background: var(--brand-blue);
  }
  .brand-name {
    font-family: "Abel", sans-serif;
    font-size: 46px;
    letter-spacing: 2px;
    color: var(--brand-blue);
    text-transform: uppercase;
    line-height: 1.1;
  }
</style>
</head>
<body>
  <main class="stage">
    <section class="business-card">
      <div class="card-arc"></div>
      <h1 class="holder-name">DENNIS MARLOW</h1>
      <ul class="contact-list">
        <li class="contact-item"><span class="contact-badge">T</span>+61 427581962</li>
        <li class="contact-item"><span class="contact-badge">F</span>dennis@qovo.com.au</li>
        <li class="contact-item"><span class="contact-badge">A</span>P.O. Box 872 Kelvindale QLD 4309</li>
      </ul>
      <div class="brand-mark">
        <span class="brand-dot"></span>
        <span class="brand-name">Qovo<br>International</span>
      </div>
    </section>
  </main>
</body>
</html>
```